Coral Sleep Depot Website

Need a design for a local Miami mattress store.
The store is called Coral Sleep Depot.
need it to be something that customers can find on the internet and will
give them my location, they need to know i have the same brand mattress as the other store except i have them at almost half the price.

the office phone number is (786)555-0143
the office address is: 4127 sw Heron Bend Ave, Miami FL 33190

included is the logo, id like to stick the with white and teal design

here are is an excerpt that can or cannot be included

"We are a premium mattress discount outlet store located in South Florida; offering Free Delivery to Broward Miami-Dade, the Keys, and Palm Beach.

We carry the best brands in the market: Varnell CloudHaven; Dorvik SpineAlign, Brackett & Lowe, Pendry, among others.

We are open 7 days a week, and we are accessible from all major highways. We are a family business and our goal is to provide you with the most comfortable and best quality mattress at a price that has no competition. Come visit us and take a look at our large inventory selection."

```html
<!DOCTYPE html>
<html lang="en">
<head>
<meta charset="utf-8">
<title>Coral Sleep Depot</title>
<link href="https://fonts.googleapis.com/css2?family=Gelasio:wght@400;700&family=Open+Sans:wght@400;600;700&display=swap" rel="stylesheet">
<style>
:root{
  --teal:#7fd4df;
  --teal-dark:#2aa9bd;
  --teal-text:#1f8e9a;
  --blue:#2b96c6;
  --blue-head:#2a8fc1;
  --ink:#2b2b2b;
  --muted:#6f6f6f;
  --panel:#f4f4f4;
  --yellow:#f6d20f;
  --navy:#0b3b5b;
  --navy-deep:#06283f;
  --line:#d6d6d6;
  --field:#eeeeee;
}
*{box-sizing:border-box;margin:0;padding:0}
html,body{width:1200px;height:2799px;overflow:hidden}
body{position:relative;background:#fff;font-family:"Open Sans",Arial,sans-serif;color:var(--ink)}
.abs{position:absolute}
.serif{font-family:"Gelasio",Georgia,serif}

/* header */
.brand{left:200px;top:44px;display:flex;align-items:center;gap:12px}
.brand-mark{width:22px;height:22px;border-radius:50%;background:var(--teal-dark)}
.brand-name{font-family:"Gelasio",Georgia,serif;font-size:27px;color:#1c3b4a}
.phone{left:868px;top:38px;display:flex;align-items:center;gap:10px;font-size:20px;color:#444}
.search{left:784px;top:78px;width:216px;height:25px;border:2px solid #bfe6ec;border-radius:4px;font-size:9px;color:#888;padding:5px 12px;letter-spacing:.5px}
.search svg{position:absolute;right:22px;top:5px}

.nav{left:0;top:123px;width:1200px;height:45px;background:var(--teal)}
.nav-rule{left:0;top:168px;width:1200px;height:9px;background:var(--teal-dark)}
.nav a{position:absolute;top:14px;font-family:"Gelasio",Georgia,serif;font-size:15px;color:#24424c;text-decoration:none;letter-spacing:.3px}
.nav .active{left:200px;width:104px;top:0;height:45px;background:var(--teal);text-align:center;padding-top:14px;border-bottom:6px solid var(--teal-dark);border-radius:0 0 6px 6px}

/* hero */
.hero{left:0;top:177px;width:1200px;height:472px;background:linear-gradient(100deg,#3a2a22 0%,#6e584b 18%,#d8c3ad 45%,#efe3d6 70%,#cdb9a7 100%)}
.hero-band{left:0;top:593px;width:1200px;height:56px;background:rgba(20,20,20,.72)}
.hero-title{left:196px;top:296px;font-size:38px;font-weight:700;color:#fff}
.hero-copy{left:198px;top:362px;font-size:17px;line-height:23px;color:#fff}
.shop{left:196px;top:463px;width:198px;height:50px;background:var(--yellow);font-size:22px;font-weight:700;color:#222;text-align:center;line-height:50px;letter-spacing:.5px}
.dots{left:198px;top:614px;display:flex;gap:6px}
.dots i{width:14px;height:14px;border-radius:50%;background:#111;display:block}
.dots i.on{background:var(--teal-dark)}
.hero-brand{left:690px;top:238px;font-family:"Gelasio",Georgia,serif;font-size:40px;color:var(--teal-dark)}

.social{left:1163px;width:37px;height:38px}
.tw{top:311px;background:#27a9e1}
.gp{top:388px;background:#d3382a}
.yt{top:427px;background:#c4302b}
.fb{left:1058px;top:351px;width:142px;height:37px;background:#3b5998;color:#fff;font-size:14px;font-weight:600;display:flex;align-items:center;gap:14px;padding-left:12px}
.fb span.sq{width:12px;height:12px;background:#fff;display:block}

/* partner badges */
.partners{left:205px;top:700px;width:790px;height:66px;display:flex;justify-content:space-between;align-items:center}
.badge{height:46px;border-radius:23px;background:#d9ecf3}
.badge.b1{width:122px;background:#cfe3f1}
.badge.b2{width:62px;border-radius:10px;background:#1a5fa8}
.badge.b3{width:70px;border-radius:50%;height:60px;background:#f2d21a}
.badge.b4{width:64px;height:62px;border-radius:8px;background:#8c8580}
.badge.b5{width:110px;background:#e9d6e4}
.badge.b6{width:78px;height:56px;border-radius:30% 30% 50% 50%;background:#173f8c}
.badge.b7{width:130px;height:34px;background:#cde4ec}

/* about */
.about{left:0;top:812px;width:1200px;height:367px;background:var(--panel);border-bottom:2px solid var(--line)}
.sec-title{width:1200px;left:0;text-align:center;font-family:"Gelasio",Georgia,serif;font-weight:700;color:#222}
.about-img{left:198px;top:918px;width:263px;height:203px;background:linear-gradient(160deg,#e9eef2,#c8ced4 60%,#9aa2aa);border:1px solid #ddd}
.about-head{left:489px;top:912px;font-size:18px;font-weight:600;color:#222}
.about-copy{left:489px;top:950px;width:508px;font-size:12.4px;line-height:20.5px;color:#8a8a8a}
.btn-line{left:489px;top:1093px;width:110px;height:28px;border:1px solid var(--teal-dark);background:#fff;font-size:12px;text-align:center;line-height:26px;color:#333}

/* products */
.products{left:0;top:1181px;width:1200px;height:625px;background:var(--panel);border-bottom:2px solid var(--line)}
.sub{left:0;width:1200px;top:1274px;text-align:center;font-family:"Gelasio",Georgia,serif;font-style:italic;font-size:14.5px;line-height:22px;color:#777}
.prod{top:1370px;width:262px;height:175px;background:#fff;border:1px solid #e2e2e2}
.prod div{position:absolute;inset:0 28px;background:linear-gradient(#555,#1e1e1e)}
.prod.p2 div{inset:0;background:linear-gradient(#f7f7f7,#e3e3e3 70%,#5a3b34 72%,#e8e8e8 80%)}
.prod.p3 div{inset:20px 10px 10px;background:linear-gradient(#fafafa,#e6e6e6 65%,#d5d5d5)}
.p-title{top:1562px;width:262px;text-align:center;font-family:"Gelasio",Georgia,serif;font-weight:700;font-size:19px;color:var(--teal-text)}
.p-copy{top:1594px;width:262px;text-align:center;font-family:"Gelasio",Georgia,serif;font-size:13px;line-height:17.5px;color:#444}
.note{left:0;width:1200px;top:1728px;text-align:center;font-size:13px;line-height:18px;color:#888}

/* contact */
.map{left:0;top:1918px;width:1200px;height:407px;background:linear-gradient(135deg,#5d6559,#7b7f72 40%,#8f8d80 70%,#6f7568)}
.info{left:438px;top:1998px;width:329px;height:167px;background:var(--blue);color:#fff}
.info .circle{position:absolute;left:18px;top:14px;width:50px;height:50px;border-radius:50%;background:#fff}
.info .mail{position:absolute;left:86px;top:26px;font-size:17px}
.info hr{position:absolute;left:18px;right:18px;top:76px;border:0;border-top:1px solid rgba(255,255,255,.45)}
.info .addr-head{position:absolute;left:18px;top:88px;font-size:13.5px;font-weight:700}
.info .row{position:absolute;left:18px;font-size:11px;font-weight:600;display:flex;gap:10px;align-items:center}

.form{left:198px;top:2226px;width:802px;height:353px;background:#fff;border-radius:6px;box-shadow:0 0 8px rgba(0,0,0,.18)}
.form h2{position:absolute;left:40px;top:30px;font-weight:400;font-size:24px;color:var(--blue-head)}
.form p{position:absolute;left:40px;top:68px;width:728px;font-size:11.5px;line-height:15.5px;color:#666}
.field{left:239px;width:300px;height:32px;background:var(--field);font-size:12px;color:#888;padding:8px 15px}
.comment{left:558px;top:2366px;width:399px;height:153px;background:var(--field);font-size:12px;color:#888;padding:8px 15px}
.submit{left:558px;top:2532px;width:97px;height:30px;border:1px solid var(--teal-dark);font-size:14px;text-align:center;line-height:28px;color:#333;background:#fff}

/* footer */
.footer{left:0;top:2622px;width:1200px;height:140px;background:var(--navy);color:#fff}
.f-head{top:44px;font-size:13.5px}
.f-rule{top:70px;height:1px;background:rgba(255,255,255,.25)}
.f-links{left:200px;top:93px;font-family:"Gelasio",Georgia,serif;font-size:11.5px;letter-spacing:.3px;display:flex;gap:16px}
.cards{left:765px;top:90px;display:flex;gap:6px}
.cards i{display:block;width:30px;height:19px;border-radius:2px}
.copy{left:0;top:2762px;width:1200px;height:37px;background:var(--navy-deep);color:#dfe6ea;font-size:11.5px;text-align:center;line-height:37px}
</style>
</head>
<body>

<header>
  <div class="abs brand"><span class="brand-mark"></span><span class="brand-name">Coral Sleep Depot</span></div>
  <div class="abs phone">
    <svg width="20" height="16" viewBox="0 0 20 16"><path d="M2 5c0-3 16-3 16 0v2h-4V5H6v2H2z" fill="#555"/><rect x="4" y="8" width="12" height="7" rx="1.5" fill="#555"/></svg>
    (786)555-0143
  </div>
  <div class="abs search">SEARCH
    <svg width="12" height="12" viewBox="0 0 12 12"><circle cx="5" cy="5" r="3.6" fill="none" stroke="#999" stroke-width="1.4"/><path d="M7.7 7.7l3.2 3.2" stroke="#999" stroke-width="1.6"/></svg>
  </div>
</header>

<nav class="abs nav">
  <a class="active" href="#">HOME</a>
  <a href="#" style="left:397px">ABOUT US</a>
  <a href="#" style="left:522px">PRODUCTS</a>
  <a href="#" style="left:680px">LOCATION</a>
  <a href="#" style="left:831px">BRANDS AND PRICES</a>
</nav>
<div class="abs nav-rule"></div>

<section>
  <div class="abs hero" role="img" aria-label="Photo of a woman sitting on a mattress in a bright bedroom with shuttered windows"></div>
  <div class="abs hero-band"></div>
  <h1 class="abs hero-title">Lowest Prices</h1>
  <p class="abs hero-copy">This is Layerpad's version &nbsp;of Lorem Ipsum.<br>Proin gravida nibh vel velit auctor aliquet.<br>Aenean sollicitudin,</p>
  <div class="abs shop">SHOP NOW</div>
  <div class="abs dots"><i></i><i></i><i></i><i class="on"></i><i></i></div>
  <div class="abs hero-brand">Coral Sleep Depot</div>

  <div class="abs social tw"></div>
  <div class="abs fb"><span class="sq"></span>Friendwall</div>
  <div class="abs social gp"></div>
  <div class="abs social yt"></div>
</section>

<section class="abs partners" aria-label="Mattress brands we carry">
  <span class="badge b1"></span><span class="badge b2"></span><span class="badge b3"></span><span class="badge b4"></span><span class="badge b5"></span><span class="badge b6"></span><span class="badge b7"></span>
</section>

<section>
  <div class="abs about"></div>
  <h2 class="abs sec-title" style="top:846px;font-size:25px">ABOUT</h2>
  <div class="abs about-img" role="img" aria-label="Photo of a woman sleeping on a mattress"></div>
  <h3 class="abs about-head">We are a discount outlet store located in South Florida delivering.</h3>
  <p class="abs about-copy">We are a discount outlet store located in South Florida; delivering to Broward Miami-Dade, the Keys, and Palm Beach. We carry the best brands in the market: Varnell CloudHaven; Dorvik SpineAlign, Brackett &amp; Lowe, Pendry, among others. We are open 7 days a week, and we are accessible from all major highways. We are a family business and our goal is to provide you with the most comfortable and best quality mattress at a price that has no competition. Come visit us and take a look at our large inventory selection.</p>
  <div class="abs btn-line">Learn More</div>
</section>

<section>
  <div class="abs products"></div>
  <h2 class="abs sec-title" style="top:1225px;font-size:25px">PRODUCTS</h2>
  <p class="abs sub">This is Layerpad's version &nbsp;of Lorem Ipsum. Proin gravida nibh vel velit<br>auctor aliquet. Aenean sollicitudin, lorem</p>

  <div class="abs prod" style="left:200px"><div role="img" aria-label="Photo of a mattress label close-up"></div></div>
  <div class="abs prod p2" style="left:468px"><div role="img" aria-label="Photo of a pillowtop king mattress"></div></div>
  <div class="abs prod p3" style="left:737px"><div role="img" aria-label="Photo of a queen mattress on a box spring"></div></div>

  <h3 class="abs p-title" style="left:200px">Varnell cloudhaven Queen</h3>
  <h3 class="abs p-title" style="left:468px">King Mattress From $299</h3>
  <h3 class="abs p-title" style="left:737px">Mattress Queen Varnell</h3>
  <p class="abs p-copy" style="left:200px">Mattress Queen pillowtop 75% OFF<br>Same day delivery!!</p>
  <p class="abs p-copy" style="left:468px">Queen Mattress from $199<br>King Mattress from $299<br>Full Mattress from $169<br>Twin Mattress from $99</p>
  <p class="abs p-copy" style="left:737px">Have a good night's sleep on<br>one of our comfortable<br>mattresses.</p>

  <p class="abs note">If you have any question concerning deliveries, pick-ups or prices, please don't hesitate to contact us. Our friendly staff will<br>help find the best solutions for you.</p>
</section>

<section>
  <h2 class="abs sec-title" style="top:1852px;font-size:30px">Contact us</h2>
  <div class="abs map" role="img" aria-label="Street map showing the store location"></div>
  <div class="abs info">
    <span class="circle"></span>
    <svg style="position:absolute;left:32px;top:30px" width="22" height="17" viewBox="0 0 22 17"><rect x="1" y="1" width="20" height="15" rx="1.5" fill="var(--blue)"/><path d="M1 2l10 8 10-8" fill="none" stroke="#fff" stroke-width="1.6"/></svg>
    <span class="mail">info@coralsleepdepot.com</span>
    <hr>
    <span class="addr-head">Address: Mattress Store</span>
    <span class="row" style="top:113px"><svg width="10" height="13" viewBox="0 0 10 13"><path d="M5 0a5 5 0 0 1 5 5c0 3.5-5 8-5 8S0 8.5 0 5a5 5 0 0 1 5-5z" fill="#fff"/><circle cx="5" cy="5" r="1.8" fill="var(--blue)"/></svg>4127 sw Heron Bend Ave, Miami FL 33190</span>
    <span class="row" style="top:137px"><svg width="10" height="13" viewBox="0 0 10 13"><rect x="2" y="0" width="6" height="13" rx="1.2" fill="#fff"/><rect x="3" y="2" width="4" height="8" fill="var(--blue)"/></svg>(786)555-0143</span>
  </div>

  <div class="abs form">
    <h2>Getting in Touch is Easy</h2>
    <p>Please complete the request form below to be contacted by a member of the Harbor Lane team. Harbor Lane respects your privacy at all times and all information shall remain confidential and will not be divulged to any other party. For further information, please see our Privacy Policy</p>
  </div>
  <div class="abs field" style="top:2366px">First Name</div>
  <div class="abs field" style="top:2407px">Last Name</div>
  <div class="abs field" style="top:2448px">Phone</div>
  <div class="abs field" style="top:2489px">Email</div>
  <div class="abs comment">Comment</div>
  <div class="abs submit">Submit</div>
</section>

<footer>
  <div class="abs footer">
    <span class="abs f-head" style="left:200px">Quick Links</span>
    <span class="abs f-head" style="left:696px">We gladly accept the following payment methods:</span>
    <span class="abs f-rule" style="left:200px;width:466px"></span>
    <span class="abs f-rule" style="left:696px;width:304px"></span>
    <div class="abs f-links"><span>HOME</span><span>|</span><span>ABOUT US</span><span>|</span><span>PRODUCTS</span><span>|</span><span>LOCATION</span><span>|</span><span>BRANDS AND PRICES</span></div>
    <div class="abs cards"><i style="background:#e9e9e9"></i><i style="background:#f4f4f4"></i><i style="background:#9fc3e6"></i><i style="background:#e6e6e6"></i><i style="background:#d9d9d9"></i></div>
  </div>
  <div class="abs copy">©Copyright 2014 . All Rights Reserved.</div>
</footer>

</body>
</html>
```